Tasman Curdworks Guild needs new business cards

We need new business cards designed and produced. We are likely to need other design work done for ads, flyers etc in future.

We would like to start with an initial business card.

The Tasman Curdworks Guild (TCG) is a membership-based not-for-profit organisation that looks after the interests of Australia's small to medium artisan cheesemakers, many of whom are also small-scale farmers. The design should be simple, using our logo, but also communicate our artisan cheese and small dairy farm focus.

The first card to be designed and produced is for me, Miriam Tolhurst. My details are:

Miriam Tolhurst
Secretary
Tasman Curdworks Guild (TCG)
http://www.curdworksguild.example
T +61452837190
E miriam.miriamtolhurst@mailbox.example

I have attached the TCG logo in jpg form. I have a higher resolution version available if needed.

Thank you!

Miriam

Miriam Tolhurst
Tasman Curdworks Guild
miriam.miriamtolhurst@mailbox.example
+61452837190

Sans Serif

• Logo (see attached file)

```html
<!DOCTYPE html>
<html lang="en">
<head>
<meta charset="utf-8">
<title>Tasman Curdworks Guild — Business Card</title>
<link rel="stylesheet" href="https://fonts.googleapis.com/css2?family=Inter:wght@300;400;600;700&display=swap">
<style>
  :root {
    --backdrop: #d9d9d7;
    --card-light: #ebe7e1;
    --card-mist: #ddd6cc;
    --card-sand: #cdb596;
    --card-gold: #c9a46a;
    --card-deep-gold: #bf9a5e;
    --ink-brown: #5b3414;
    --ink-white: #ffffff;
    --ink-soft: #f3e9d8;
  }
  * { margin: 0; padding: 0; box-sizing: border-box; }
  html, body {
    width: 1200px;
    height: 895px;
    overflow: hidden;
    background: var(--backdrop);
  }
  .canvas {
    position: relative;
    width: 1200px;
    height: 895px;
    display: flex;
    align-items: center;
    justify-content: center;
  }
  .business-card {
    position: relative;
    width: 530px;
    height: 820px;
    border-radius: 4px;
    overflow: hidden;
    box-shadow: 0 10px 30px rgba(0,0,0,0.18);
    font-family: "Inter", "Helvetica Neue", Arial, sans-serif;
  }
  .card-texture {
    position: absolute;
    inset: 0;
    background: linear-gradient(180deg,
      var(--card-light) 0%,
      var(--card-mist) 48%,
      var(--card-sand) 56%,
      #d9c9b2 60%,
      var(--card-gold) 68%,
      var(--card-deep-gold) 100%);
  }
  .guild-mark {
    position: absolute;
    left: 56px;
    top: 120px;
    display: flex;
    flex-direction: column;
    gap: 18px;
  }
  .guild-dot {
    width: 84px;
    height: 84px;
    border-radius: 50%;
    background: var(--card-gold);
  }
  .guild-name {
    color: var(--ink-brown);
    font-weight: 400;
    font-size: 40px;
    line-height: 1.05;
  }
  .contact-block {
    position: absolute;
    right: 48px;
    top: 490px;
    text-align: right;
  }
  .person-name {
    color: var(--ink-white);
    font-weight: 300;
    font-size: 34px;
    line-height: 1.1;
  }
  .person-role {
    color: var(--ink-soft);
    font-weight: 600;
    font-size: 19px;
    margin-bottom: 40px;
  }
  .contact-line {
    color: var(--ink-brown);
    font-size: 20px;
    font-weight: 400;
    line-height: 1.45;
  }
  .contact-line.website { font-weight: 700; }
  .contact-line .label { font-weight: 700; }
  .contact-line.email { font-size: 17px; }
</style>
</head>
<body>
  <main class="canvas">
    <article class="business-card">
      <div class="card-texture" role="img" aria-label="Textured cheese rind surface fading from pale cream to golden tan"></div>
      <div class="guild-mark">
        <span class="guild-dot"></span>
        <p class="guild-name">Tasman<br>Curdworks<br>Guild</p>
      </div>
      <div class="contact-block">
        <p class="person-name">Miriam Tolhurst</p>
        <p class="person-role">Secretary</p>
        <p class="contact-line website">www.curdworksguild.example</p>
        <p class="contact-line"><span class="label">t:</span> +61452837190</p>
        <p class="contact-line email"><span class="label">e:</span> miriam.miriamtolhurst@mailbox.example</p>
      </div>
    </article>
  </main>
</body>
</html>
```